KVT New York

i need a marketing piece for my upcoming live dental hands on course. highlighting that it is in new york, with photo of new york city or sky line

```html
<!DOCTYPE html>
<html lang="en">
<head>
<meta charset="UTF-8">
<title>KVT – 2 Days Hands On Workshop in New York</title>
<link rel="stylesheet" href="https://fonts.googleapis.com/css2?family=Barlow+Condensed:ital,wght@0,500;0,600;0,700;0,800;1,700&family=Montserrat:wght@500;800&display=swap">
<style>
  :root {
    --page-bg: #e8e9eb;
    --sky-top: #c3e6f8;
    --sky-mid: #eaf6fd;
    --sky-low: #ffffff;
    --ink: #0b0b0b;
    --ink-soft: #2f2f2f;
    --accent: #0a7ec2;
    --accent-bright: #1aa3e8;
    --navy: #074a7a;
    --navy-light: #3a78a3;
    --button-top: #ffffff;
    --button-bottom: #58c3f0;
  }
  * { box-sizing: border-box; margin: 0; padding: 0; }
  html, body { width: 1200px; height: 1168px; overflow: hidden; }
  body { background: var(--page-bg); position: relative; font-family: "Barlow Condensed", "Arial Narrow", sans-serif; }

  .flyer {
    position: absolute; left: 82px; top: 65px; width: 1037px; height: 1037px;
    overflow: hidden; border-radius: 4px;
    background: radial-gradient(ellipse 70% 60% at 40% 65%, var(--sky-low) 0%, var(--sky-mid) 55%, var(--sky-top) 100%);
  }

  .skyline {
    position: absolute; left: 0; top: 700px; width: 730px; height: 337px;
    background: linear-gradient(180deg, rgba(58,120,163,0) 0%, var(--navy-light) 20%, #1f5f8f 45%, var(--navy) 65%, var(--navy) 100%);
  }

  .photo { position: absolute; left: 0; top: 0; width: 1037px; height: 1037px; }

  .brand { position: absolute; left: 64px; top: 66px; display: flex; align-items: center; gap: 16px; }
  .brand-name { font-family: "Montserrat", sans-serif; font-weight: 800; font-size: 76px; line-height: 1; color: var(--ink); letter-spacing: 1px; }
  .brand-tagline { font-family: "Montserrat", sans-serif; font-weight: 500; font-size: 24px; line-height: 1.1; color: #1d1d1d; }

  .headline { position: absolute; left: 58px; top: 164px; color: var(--ink); }
  .headline-top { font-size: 76px; font-weight: 500; line-height: 1; letter-spacing: -0.5px; }
  .headline-top strong { color: var(--accent); font-weight: 700; }
  .headline-main { font-size: 116px; font-weight: 800; line-height: 0.95; letter-spacing: 0.5px; }

  .rule { position: absolute; left: 60px; height: 3px; background: linear-gradient(90deg, var(--accent) 0%, rgba(10,126,194,0.6) 60%, rgba(10,126,194,0) 100%); }
  .rule-top { top: 355px; width: 360px; }
  .rule-bottom { top: 482px; width: 380px; }

  .event-date { position: absolute; left: 58px; top: 370px; font-size: 58px; font-weight: 700; line-height: 1; color: var(--ink); letter-spacing: -0.5px; }
  .event-venue { position: absolute; left: 58px; top: 432px; font-size: 37px; font-weight: 600; line-height: 1; color: var(--ink); }

  .benefits { position: absolute; left: 53px; top: 510px; list-style: none; width: 612px; }
  .benefits li { position: relative; padding-left: 32px; font-size: 33px; font-weight: 500; line-height: 42px; color: var(--ink-soft); letter-spacing: -0.4px; }
  .benefits svg { position: absolute; left: 0; top: 11px; width: 22px; height: 22px; }

  .cta-arrows { position: absolute; left: 138px; top: 896px; width: 80px; height: 88px; }
  .cta-button {
    position: absolute; left: 280px; top: 889px; width: 342px; height: 59px; border-radius: 30px;
    background: linear-gradient(180deg, var(--button-top) 0%, #d8f0fb 45%, var(--button-bottom) 100%);
    display: flex; align-items: center; justify-content: center;
    font-size: 41px; font-weight: 700; font-style: italic; color: var(--ink-soft);
  }
  .cta-site { position: absolute; left: 280px; top: 956px; width: 342px; text-align: center; font-family: "Montserrat", sans-serif; font-weight: 800; font-style: italic; font-size: 28px; color: #ffffff; }
  .cta-site span { color: var(--accent-bright); }
</style>
</head>
<body>
  <main class="flyer">
    <div class="skyline" role="img" aria-label="New York City skyline silhouette with the Brooklyn Bridge, the Statue of Liberty and Manhattan towers"></div>

    <svg class="photo" viewBox="0 0 1037 1037" role="img" aria-label="Close-up photo of a smiling mouth with metal braces">
      <defs>
        <linearGradient id="skinTone" x1="0" y1="0" x2="1" y2="1">
          <stop offset="0" stop-color="#eebc9f"/>
          <stop offset="0.45" stop-color="#f5d2bb"/>
          <stop offset="0.6" stop-color="#eaa795"/>
          <stop offset="1" stop-color="#f3cdb3"/>
        </linearGradient>
      </defs>
      <path d="M551,0 C620,120 700,350 712,560 C718,720 660,830 726,1037 L1037,1037 L1037,0 Z" fill="url(#skinTone)"/>
    </svg>

    <div class="brand">
      <span class="brand-name">KVT</span>
      <span class="brand-tagline">Kinetic Vector<br>Training</span>
    </div>

    <h1 class="headline">
      <div class="headline-top"><strong>2 DAYS</strong> HANDS ON</div>
      <div class="headline-main">WORKSHOP</div>
    </h1>

    <div class="rule rule-top"></div>
    <p class="event-date">May 23rd - 24th, 2025</p>
    <p class="event-venue">in New York at the Riverbend Hotel</p>
    <div class="rule rule-bottom"></div>

    <ul class="benefits">
      <li><svg viewBox="0 0 24 24"><rect x="2" y="4" width="17" height="17" rx="2" fill="none" stroke="#0a7ec2" stroke-width="2.2"/><path d="M6 12l4 4 11-12" fill="none" stroke="#0a7ec2" stroke-width="2.6" stroke-linecap="round" stroke-linejoin="round"/></svg>Understand how teeth move and how to move them</li>
      <li><svg viewBox="0 0 24 24"><rect x="2" y="4" width="17" height="17" rx="2" fill="none" stroke="#0a7ec2" stroke-width="2.2"/><path d="M6 12l4 4 11-12" fill="none" stroke="#0a7ec2" stroke-width="2.6" stroke-linecap="round" stroke-linejoin="round"/></svg>Improve the success rates of your Alignova cases</li>
      <li><svg viewBox="0 0 24 24"><rect x="2" y="4" width="17" height="17" rx="2" fill="none" stroke="#0a7ec2" stroke-width="2.2"/><path d="M6 12l4 4 11-12" fill="none" stroke="#0a7ec2" stroke-width="2.6" stroke-linecap="round" stroke-linejoin="round"/></svg>Orthodontics is the key to better Implant, Veneer and FMR outcomes</li>
    </ul>

    <svg class="cta-arrows" viewBox="0 0 80 88" aria-hidden="true">
      <path d="M0 18 L40 44 L0 70 L24 44 Z" fill="#1aa3e8"/>
      <path d="M20 0 L80 44 L20 88 L52 44 Z" fill="#1aa3e8"/>
    </svg>
    <div class="cta-button">Register Today</div>
    <p class="cta-site"><span>at</span> motivecourse.com</p>
  </main>
</body>
</html>
```